R.T. Framers Postcard Design

We need a postcard designed around the utility rebates for window installations. For customers who have Electric heated homes can receive $6 per square foot for each window and patio door and for Natural gas heated homes, they can get $75.00 per window and patio door. The $6 per square foot for electric heated customers is the better rebate averaging about $1000.00 for a house with 10 windows and a patio door. Our Company colors are maroon, black and white, we would like to have a post card designed around these colors. The postcard should be designed to share about these 2 rebates and having a window installation theme. You can use pictures off of our website...www.rtframers-example.com

Target Market(s)

Homeowners with electric heat or Natural gas heat

Industry/Entity Type

Utility

Requirements
Must have
• Blank white square on the back for me to hand write address information.

```html
<!DOCTYPE html>
<html lang="en">
<head>
<meta charset="utf-8">
<title>R.T. Framers Postcard</title>
<link rel="stylesheet" href="https://fonts.googleapis.com/css2?family=Source+Sans+3:wght@400;600;700&display=swap">
<style>
  :root {
    --maroon: #7e1416;
    --ink: #111111;
    --paper: #ffffff;
    --card-grey: #e4e4e4;
    --stage: #2b2b2b;
    --address-box: #e7d8d4;
    --sky-top: #bfe3f5;
    --sky-bottom: #e8f4fa;
    --badge: #2f8f5a;
  }
  * { margin: 0; padding: 0; box-sizing: border-box; }
  html, body {
    width: 1200px; height: 1079px; overflow: hidden;
    background: var(--stage);
    font-family: "Source Sans 3", "Myriad Pro", Arial, sans-serif;
  }
  .canvas { position: relative; width: 1200px; height: 1079px; }

  .card { position: absolute; width: 707px; height: 548px; overflow: hidden; }

  /* Back side */
  .card-back {
    left: 50px; top: 50px;
    background:
      linear-gradient(135deg, transparent 55%, rgba(0,0,0,0.05) 56%, transparent 75%),
      linear-gradient(200deg, rgba(0,0,0,0.07) 0%, transparent 45%),
      linear-gradient(160deg, transparent 60%, rgba(0,0,0,0.06) 61%, transparent 80%),
      var(--paper);
  }
  .brand { position: absolute; display: flex; align-items: center; gap: 10px; }
  .brand-square { width: 50px; height: 50px; background: var(--maroon); }
  .brand-name {
    font-weight: 700; font-size: 56px; line-height: 1; color: var(--maroon);
    letter-spacing: 0.5px;
  }
  .tagline {
    position: absolute; font-size: 17px; color: var(--maroon); letter-spacing: 0.1px;
  }
  .card-back .brand { left: 35px; top: 38px; }
  .card-back .tagline { left: 35px; top: 97px; }
  .rebate-copy {
    position: absolute; left: 35px; top: 124px; width: 480px;
    font-size: 18px; line-height: 23.5px; color: var(--ink);
  }
  .choice-note {
    position: absolute; left: 35px; top: 322px; width: 310px;
    font-size: 16.5px; line-height: 21px; color: var(--maroon);
  }
  .site-note {
    position: absolute; left: 35px; top: 399px;
    font-size: 16.5px; line-height: 21px; color: var(--maroon);
  }
  .site-note .url { color: var(--ink); font-size: 18px; }
  .address-box {
    position: absolute; left: 538px; top: 23px; width: 144px; height: 145px;
    background: var(--address-box);
  }

  /* Front side */
  .card-front {
    left: 452px; top: 490px; background: var(--card-grey);
    box-shadow: 0 0 20px rgba(0,0,0,0.35);
  }
  .corner { position: absolute; left: 0; top: 0; }
  .card-front .brand { left: 168px; top: 42px; }
  .card-front .tagline { left: 168px; top: 103px; }

  .photo { position: absolute; border: 2px solid #fff; }
  .photo-frame { position: absolute; background: var(--maroon); }
  .photo-room-a { background: linear-gradient(90deg, #e9e6df, #cbbfa8); }
  .photo-room-b { background: linear-gradient(180deg, #f2f1ee, #b9b3a8 70%, #8a3b2f); }
  .photo-room-c { background: linear-gradient(180deg, #cfd6a4, #8b7a4a 60%, #4f5a3e); }
  .photo-room-d { background: linear-gradient(180deg, #d7c2a0, #9a6a45 60%, #6b3f2a); }

  .window-scene {
    position: absolute; left: 192px; top: 150px; width: 346px; height: 275px;
    background: linear-gradient(180deg, var(--sky-top), var(--sky-bottom));
    border: 8px solid #f6f6f6;
    box-shadow: 0 2px 6px rgba(0,0,0,0.15);
  }
  .quote {
    position: absolute; left: 222px; top: 192px; width: 170px;
    font-size: 24px; line-height: 29.5px; color: #1a1a1a; letter-spacing: 0.3px;
  }
  .badge {
    position: absolute; left: 222px; top: 382px; width: 56px; height: 22px;
    background: var(--badge);
  }
  .badge-label {
    position: absolute; left: 286px; top: 379px;
    font-size: 10.5px; line-height: 13px; color: var(--ink);
  }
  .contact-address {
    position: absolute; left: 0; width: 707px; top: 445px; text-align: center;
    font-size: 16.5px; color: var(--maroon);
  }
  .contact-lines {
    position: absolute; left: 0; width: 707px; top: 469px; text-align: center;
    font-size: 14.5px; color: var(--ink); word-spacing: 1px;
  }
  .contact-lines span + span { margin-left: 14px; }
  .footer-band {
    position: absolute; left: 0; top: 497px; width: 707px; height: 51px;
    background: var(--maroon); color: var(--paper);
    font-size: 18px; text-align: center; line-height: 26px; padding-top: 0;
  }
</style>
</head>
<body>
<div class="canvas">

  <section class="card card-back" aria-label="Postcard back">
    <div class="brand">
      <div class="brand-square"></div>
      <div class="brand-name">R.T. FRAMERS</div>
    </div>
    <p class="tagline">YOUR LEADER IN QUALITY WINDOW INSTALLATIONS</p>
    <p class="rebate-copy">Who have Electric heated homes can receive $6 per square foot for each window and patio door and for Natural gas heated homes, they can get $75.00<br>per window and patio door.<br>The $6 per square foot for electric<br>heated customers is the better rebate<br>averaging about $1000.00 for a house<br>with 10 windows and a patio door.</p>
    <p class="choice-note">For customers with electrically heated homes, you now have a choice of how to pay for energy-saving home</p>
    <p class="site-note">For more info visit our site<br><span class="url">www.rtframers-example.com</span></p>
    <div class="address-box" aria-label="Space for handwritten address"></div>
  </section>

  <section class="card card-front" aria-label="Postcard front">
    <svg class="corner" width="176" height="127" viewBox="0 0 176 127" aria-hidden="true">
      <polygon points="0,0 176,0 0,127" fill="var(--maroon)"/>
    </svg>
    <div class="brand">
      <div class="brand-square"></div>
      <div class="brand-name">R.T. FRAMERS</div>
    </div>
    <p class="tagline">YOUR LEADER IN QUALITY WINDOW INSTALLATIONS</p>

    <div class="photo-frame" style="left:17px;top:187px;width:90px;height:60px;"></div>
    <div class="photo photo-room-a" style="left:25px;top:193px;width:150px;height:102px;" role="img" aria-label="Photo of a woman standing by new bright windows"></div>

    <div class="photo-frame" style="left:110px;top:330px;width:62px;height:72px;"></div>
    <div class="photo photo-room-b" style="left:46px;top:315px;width:120px;height:82px;" role="img" aria-label="Photo of a sunroom with white framed windows"></div>

    <div class="photo-frame" style="left:620px;top:150px;width:70px;height:60px;"></div>
    <div class="photo photo-room-c" style="left:563px;top:157px;width:122px;height:78px;" role="img" aria-label="Photo of a living room with large windows and a sofa"></div>

    <div class="photo-frame" style="left:536px;top:276px;width:90px;height:66px;"></div>
    <div class="photo photo-room-d" style="left:540px;top:251px;width:112px;height:86px;" role="img" aria-label="Photo of a warm sitting room with wooden framed windows"></div>

    <div class="window-scene" role="img" aria-label="Photo of an open white window onto blue sky with a child reading on the sill"></div>
    <p class="quote">"INSTALLING WINDOWS THE RIGHT WAY EVERY TIME SINCE 1985"</p>
    <div class="badge" aria-label="Utility partner badge"></div>
    <p class="badge-label">Registered<br>Installer</p>

    <p class="contact-address">1720 Harbor Lane NE&nbsp; Cedarvale&nbsp; Washington 98100&nbsp; United States</p>
    <p class="contact-lines"><span>Email: admin@rtframers-example.com</span><span>Telephone:&nbsp; 360-555-0142</span><span>Mobile Phone Number:&nbsp; 425-555-0187</span></p>
    <div class="footer-band"><span style="display:block;padding-top:4px;">www.rtframers-example.com</span></div>
  </section>

</div>
</body>
</html>
```